New Hire Training Collateral Package ( 6 8.5 x 11 flyer designs)

I'm part of a start up company that has just received a tremendous opportunity that will ultimately allow us to grow our business exponentially (we're really excited) With that in mind, I've been tasked with building our the new hire training program. Imagine your first day at a new company; what are some of the things you need to know.. the core values, mission, vision and values, who your clients and coworkers are... the task is essentially endless HOWEVER ultimately (without scaring them away) the designs should be fun light and exciting! I'm looking for someone to help me grow that vision. See color scheme and original plan in tact. I really liked where these were going and then I lost all our files.. (rookie mistake)

Target Market(s)

Employess

Industry/Entity Type

Financial Service

Font styles to use
Sans Serif

Colors
33b8a4
000000
ffffff

Requirements
Must have
• I'm new to explaining what I want in this format but I believe the below should help: I am looking for a single letter sized flyer for the flyer titles I name below. One for each. You'd be helping me create the templates so I can enter any additional information needed in the text should anything change or need to be altered per employee.
• NEEDS: letter sized flyer (think a normal sized sheet of printer paper), please make sure the page layout is set to 8.5"x11".
• Core Values
• Mission, Vision and Values - A tempate doesn't exist yet
• Employee Profile (Meet the Team)
• Team Hierarchy (Who Rules)
• Company History (Milestone)
• Client Information Doc
• FONTS AND COLORS BELOW
• Aqua
• R: 80
• G: 227
• B: 227
• A: 100
• Hex: 50EE3
• Dark Teal:
• R: 5
• G: 92
• B: 117
• A: 100
• Hex: 055C75
• White:
• R: 225
• G: 225
• B: 225
• A: 100
• Hex: FFF
• Black:
• R: 0
• G: 0
• B: 0
• A: 100
• (pops of color like i have in the flyer examples attached can be included)
• Font: Roboto
Nice to have
• Other suggestions welcome!

```html
<!DOCTYPE html>
<html lang="en">
<head>
<meta charset="utf-8">
<title>Our Core Values – The Meridon Group</title>
<link rel="stylesheet" href="https://fonts.googleapis.com/css2?family=Roboto:wght@300;400;500;700&display=swap">
<style>
  :root {
    --teal: #33b8a4;
    --aqua: #2ab6c4;
    --black: #000000;
    --ink: #111213;
    --white: #ffffff;
    --soft: #e9eeee;
  }
  * { box-sizing: border-box; margin: 0; padding: 0; }
  html, body { width: 927px; height: 1200px; overflow: hidden; background: var(--white); }
  body { font-family: 'Roboto', Arial, sans-serif; }

  .flyer { position: relative; width: 927px; height: 1200px; background: var(--white); overflow: hidden; }

  .hero-photo {
    position: absolute; left: 0; top: 0; width: 927px; height: 472px;
    background: linear-gradient(100deg, #cfcac2 0%, #9b9489 30%, #6d665d 55%, #4a4743 80%, #3a3a38 100%);
  }

  .content-band {
    position: absolute; left: 0; top: 476px; width: 927px; height: 655px;
    background: radial-gradient(ellipse at 50% 45%, #2b2c2d 0%, #161718 60%, #0b0b0c 100%);
  }

  .title-banner {
    position: absolute; left: 495px; top: 0; width: 376px; height: 549px;
    background: var(--teal);
    clip-path: polygon(0 0, 100% 0, 100% 88.7%, 50% 100%, 0 88.7%);
    color: var(--white); text-align: center;
  }
  .brand-name {
    position: absolute; top: 150px; left: 0; width: 100%;
    font-weight: 300; font-size: 22px; letter-spacing: 0.2em; white-space: nowrap;
  }
  .banner-title {
    position: absolute; top: 205px; left: 0; width: 100%;
    font-weight: 700; font-size: 68px; line-height: 82px; letter-spacing: 0.01em;
  }
  .banner-divider { position: absolute; top: 371px; left: 55px; width: 266px; height: 8px; }
  .banner-intro {
    position: absolute; top: 397px; left: 32px; width: 312px;
    font-size: 18px; line-height: 23px; font-weight: 400;
    text-align: justify; text-align-last: center;
  }

  .drives-heading {
    position: absolute; left: 54px; top: 546px;
    color: var(--white); font-weight: 700; font-size: 42px; letter-spacing: 0.005em;
  }
  .drives-intro {
    position: absolute; left: 54px; top: 611px; width: 840px;
    color: var(--white); font-size: 19.5px; line-height: 24.5px; font-weight: 400;
  }

  .value { position: absolute; top: 738px; width: 152px; color: var(--white); text-align: center; }
  .value-icon { display: block; margin: 0 auto; width: 110px; height: 110px; }
  .value-name { margin-top: 34px; font-weight: 500; font-size: 19.5px; letter-spacing: 0.01em; }
  .value-text {
    margin-top: 14px; font-size: 10.4px; line-height: 12.6px; font-weight: 400;
    text-align: justify; text-align-last: center; color: var(--soft);
  }
  .value--integrity { left: 23px; }
  .value--communication { left: 192px; }
  .value--service { left: 379px; }
  .value--newfangled { left: 564px; }
  .value--curiosity { left: 744px; }

  .site-url {
    position: absolute; left: 0; top: 1131px; width: 927px; height: 69px;
    display: flex; align-items: center; justify-content: center;
    font-size: 23px; font-weight: 400; letter-spacing: 0.42em; color: var(--ink);
  }
</style>
</head>
<body>
<main class="flyer">
  <div class="hero-photo" role="img" aria-label="Photo of a team working together at a long table in a bright office with tall windows"></div>
  <div class="content-band"></div>

  <header class="title-banner">
    <p class="brand-name">THE MERIDON GROUP</p>
    <h1 class="banner-title">OUR CORE<br>VALUES</h1>
    <svg class="banner-divider" viewBox="0 0 266 8" aria-hidden="true">
      <line x1="0" y1="4" x2="266" y2="4" stroke="#ffffff" stroke-width="1.5"/>
      <circle cx="133" cy="4" r="3.5" fill="#ffffff"/>
      <circle cx="115" cy="4" r="2" fill="#ffffff"/>
    </svg>
    <p class="banner-intro">The Meridon Group offers a unique value proposition for the practice management consulting and revenue cycle management verticals.</p>
  </header>

  <h2 class="drives-heading">WHAT DRIVES US?</h2>
  <p class="drives-intro">At The Meridon Group, we want to always do the best, be our best, and exemplify the best. Easier said than done and not always easy to figure what that means in plain English.&nbsp; So here&nbsp; is our cheesy, but genuine description of the culture that we strive to create, nurture, and uphold day in and day out..</p>

  <section class="value value--integrity">
    <svg class="value-icon" viewBox="0 0 110 110" aria-hidden="true">
      <circle cx="55" cy="55" r="50" fill="none" stroke="var(--aqua)" stroke-width="10"/>
      <rect x="41" y="52" width="28" height="22" rx="3" fill="none" stroke="#fff" stroke-width="2.5"/>
      <path d="M46 52 V44 a9 9 0 0 1 18 0 V52" fill="none" stroke="#fff" stroke-width="2.5"/>
      <circle cx="55" cy="63" r="2.5" fill="#fff"/>
    </svg>
    <h3 class="value-name">INTEGRITY</h3>
    <p class="value-text">This one is a no-brainer. Integrity drives how we work and how we make our decisions on the most basic levels and in the most ubiquitous of ways. Trust, appropriate decision making, and honor are key in every single thing we do so this just make sense as our top value.</p>
  </section>

  <section class="value value--communication">
    <svg class="value-icon" viewBox="0 0 110 110" aria-hidden="true">
      <circle cx="55" cy="55" r="50" fill="none" stroke="var(--aqua)" stroke-width="10"/>
      <path d="M67 48 A14 14 0 1 1 55 41" fill="none" stroke="#fff" stroke-width="2.5"/>
      <path d="M52 35 L59 41 L52 47" fill="none" stroke="#fff" stroke-width="2.5"/>
    </svg>
    <h3 class="value-name">COMMUNICATION</h3>
    <p class="value-text">To us there is no such thing as being “too communicative.” We strive to be scary-fast responsive, but not to the detriment of poise, knowledge, and accuracy. We aim to collaborate and we are not afraid to ask questions. Working in a remote capacity and aiming to provide the feel of an in-house employee, it is important we stay communicative as possible ..so we made is part of who we are</p>
  </section>

  <section class="value value--service">
    <svg class="value-icon" viewBox="0 0 110 110" aria-hidden="true">
      <circle cx="55" cy="55" r="50" fill="none" stroke="var(--aqua)" stroke-width="10"/>
      <path d="M42 56 L51 65 L69 45" fill="none" stroke="#fff" stroke-width="3"/>
    </svg>
    <h3 class="value-name">SERVICE</h3>
    <p class="value-text">Ultimately, this is who we are ...a service company.&nbsp; We want our clients to feel we are in this together and simply put, it's because we are.&nbsp; Our goals aren't just problem solving and completing tasks.&nbsp; It's about making sure the person we are serving gets what they're looking for and more!&nbsp; We want to go above and beyond in respect and courteousness, maintain a high level of empathy, and always remember to take the initiative.</p>
  </section>

  <section class="value value--newfangled">
    <svg class="value-icon" viewBox="0 0 110 110" aria-hidden="true">
      <circle cx="55" cy="55" r="50" fill="none" stroke="var(--aqua)" stroke-width="10"/>
      <path d="M55 38 L59.5 50 L72 50.5 L62 58 L65.5 70 L55 63 L44.5 70 L48 58 L38 50.5 L50.5 50 Z" fill="none" stroke="#fff" stroke-width="2.3" stroke-linejoin="round"/>
    </svg>
    <h3 class="value-name">NEWFANGLED</h3>
    <p class="value-text">Kind of a weird one right (not even a noun in this context like the rest of our values)?&nbsp; Well so are we... kind of.&nbsp; It's defined as objectively new or different to be exact.&nbsp; We encourage our staff think outside the box... how can we set ourselves apart? One of the great things about our company and our team is that we do things a bit</p>
  </section>

  <section class="value value--curiosity">
    <svg class="value-icon" viewBox="0 0 110 110" aria-hidden="true">
      <circle cx="55" cy="55" r="50" fill="none" stroke="var(--aqua)" stroke-width="10"/>
      <circle cx="51" cy="51" r="11" fill="none" stroke="#fff" stroke-width="2.5"/>
      <line x1="59" y1="59" x2="69" y2="69" stroke="#fff" stroke-width="3" stroke-linecap="round"/>
    </svg>
    <h3 class="value-name">CURIOSITY</h3>
    <p class="value-text">We have a secret...we don't really know what we're doing. I mean we kind of do, but we learn every single day. The burning desire to learn new things, figure out what we don't know and tackle new tasks is the single most important attribute that will continue to drive our company to the forefront of our industry. The more you learn, the more we grow so stay interested and curious</p>
  </section>

  <footer class="site-url">themeridongroup.com</footer>
</main>
</body>
</html>
```